Development of musical artist Darvin Koltz's Website

I need a website designed for a reggae musical artist by the name of Darvin Koltz. The site should be representative of a Reggae artist from Jamaica that has a Caribbean appeal but also attractive to global audiences. The website should be responsive for all devices (desktop, laptop, mobile). It should be optimized for SEO purposes. Icons for Instagram, Facebook, Twitter, YouTube should be included. The sections of the website should be as follows: Home, Media, News, Bio, Join, Contact. The 'Join' section should be a form for database collection to the fan club. I would like to easily be able to dump this database in an excel or .csv file at any given time. The 'Media' section should be able to showcase video thumbnails and allow persons to play videos through the site and the videos will be fed from YouTube. The 'News' section will be for announcements and or new releases where the artist is mentioned. The site should also be built in such a way that analytics can be easily implemented. This website should be the main call to action for this artist moving forward. I would also like the website to have a easy to use CMS platform (Wordpress perhaps). The URL for the website will be darvinkoltzstar.example. Here are the links for some of the social media pages:
YouTube - https://www.vidstreamo.example/user/DarvinKoltz
Instagram - https://www.snapgrama.example/darvinkoltz/
A good website to refer to from a design perspective is https://velmaroots.example/

Target Market(s)

Reggae and Pop music fans

Industry/Entity Type

Artists

Coding

Coded - Design and coding required

Number of Pages Required

5+ page

Font styles to use
Sans Serif

Requirements
Must have
• Great design
Nice to have
• Parallax technology

```html
<!DOCTYPE html>
<html lang="en">
<head>
<meta charset="utf-8">
<title>Darvin Koltz — Official Site</title>
<link href="https://fonts.googleapis.com/css2?family=Orbitron:wght@500;700&family=Open+Sans:wght@400;600&family=Permanent+Marker&display=swap" rel="stylesheet">
<style>
:root{
  --red:#d4121e;
  --red-deep:#8e0c14;
  --ink:#0c0c0c;
  --charcoal:#2a2a2a;
  --sand:#ece4d3;
  --white:#ffffff;
  --muted:#bdbdbd;
  --text-dark:#222222;
}
*{box-sizing:border-box;margin:0;padding:0}
html,body{width:1200px;height:5042px;overflow:hidden}
body{position:relative;background:var(--sand);font-family:"Open Sans",Arial,sans-serif;color:var(--white)}
.display{font-family:"Orbitron",Arial,sans-serif}
.block{position:absolute;left:0;width:1200px}

/* header + hero */
.hero{top:0;height:672px;background:linear-gradient(90deg,#070707 0%,#141010 45%,#3a1a14 70%,#1a0c0a 100%)}
.hero-photo{position:absolute;right:0;top:108px;width:720px;height:564px;background:radial-gradient(ellipse at 55% 45%,#5a3226 0%,#2b1611 45%,rgba(10,8,8,0) 80%)}
.topbar{position:absolute;top:0;left:0;width:1200px;height:108px;background:#060606;border-bottom:6px solid var(--red)}
.brand{position:absolute;left:111px;top:40px;display:flex;align-items:center;gap:12px;font-family:"Orbitron",Arial,sans-serif;font-weight:700;font-size:22px;color:var(--white)}
.brand-dot{width:14px;height:14px;border-radius:50%;background:var(--red)}
.nav{position:absolute;top:44px;left:0;width:1200px;font-family:"Orbitron",Arial,sans-serif;font-size:14px;font-weight:500}
.nav a{position:absolute;color:var(--white);text-decoration:none}
.nav a.active{color:var(--red)}
.hero-title{position:absolute;left:111px;top:300px;font-family:"Orbitron",Arial,sans-serif;font-weight:700;font-size:40px;color:var(--white)}
.hero-text{position:absolute;left:111px;top:382px;width:405px;font-size:13px;line-height:24px;color:#e6e6e6}
.btn-red{position:absolute;display:flex;align-items:center;justify-content:center;background:var(--red);color:var(--white);border-radius:24px;font-family:"Orbitron",Arial,sans-serif;font-size:13px}

/* media */
.section-title{position:absolute;left:0;width:1200px;text-align:center;font-family:"Orbitron",Arial,sans-serif;font-weight:700;font-size:44px;color:var(--ink)}
.video-main{position:absolute;left:235px;top:800px;width:733px;height:393px;background:linear-gradient(135deg,#5b3a1c,#8d6b3c 40%,#3b2a1a 75%,#1c140c)}
.play{position:absolute;width:70px;height:70px;border-radius:50%;background:rgba(0,0,0,.72);display:flex;align-items:center;justify-content:center}
.video-bar{position:absolute;left:0;bottom:0;width:100%;height:30px;background:rgba(0,0,0,.75)}
.video-bar i{position:absolute;left:10px;right:10px;top:6px;height:4px;background:#555}
.video-bar b{position:absolute;left:10px;top:6px;width:12px;height:4px;background:var(--red)}
.thumb{position:absolute;top:1210px;height:144px}

/* banners */
.banner{clip-path:polygon(0 0,100% 20%,100% 100%,0 100%)}
.banner-word{position:absolute;left:0;width:1200px;text-align:center;font-family:"Permanent Marker",cursive;font-size:88px;color:var(--white)}
.banner-rule{position:absolute;left:415px;width:370px;height:4px;background:var(--white)}

/* news */
.news{top:2000px;height:560px;background:var(--charcoal)}
.card{position:absolute;top:57px;width:314px}
.card-img{height:228px}
.card h3{margin-top:31px;font-family:"Orbitron",Arial,sans-serif;font-weight:500;font-size:13px;letter-spacing:.3px}
.card .date{margin-top:10px;font-size:10px;color:var(--red)}
.card p{margin-top:8px;font-size:10.5px;line-height:20px;color:var(--muted)}
.btn-line{display:inline-flex;align-items:center;justify-content:center;border:1px solid var(--white);color:var(--white);font-family:"Orbitron",Arial,sans-serif;font-size:12px;border-radius:3px}
.card .btn-line{margin-top:22px;width:106px;height:40px}

/* bio */
.bio{top:3176px;height:490px;background:linear-gradient(90deg,#6f0a10 0%,var(--red-deep) 35%,#c5141d 100%)}
.portrait{position:absolute;left:157px;top:44px;width:320px;height:320px;border-radius:50%;border:6px solid #e23a40;background:radial-gradient(circle at 50% 45%,#6a3a2a,#2a140e 75%)}
.bio-name{position:absolute;left:531px;top:66px;font-family:"Orbitron",Arial,sans-serif;font-weight:700;font-size:28px}
.bio-date{position:absolute;left:531px;top:110px;font-size:11px;color:#f0d0d0}
.bio-text{position:absolute;left:531px;width:560px;font-size:11.5px;line-height:20px;color:#f4e6e6}

/* join */
.join-lead{position:absolute;left:220px;top:4298px;width:760px;text-align:center;font-family:"Orbitron",Arial,sans-serif;font-weight:500;font-size:16px;line-height:24px;color:var(--text-dark);text-transform:uppercase}
.field{position:absolute;left:360px;width:480px;height:42px;background:var(--white);border:1px solid #d6d0c4;color:#555;font-size:12px;padding:13px 14px}

/* footer */
.footer{top:4690px;height:352px;background:var(--ink)}
.footer-brand{position:absolute;left:0;top:100px;width:1200px;display:flex;justify-content:center;align-items:center;gap:12px;font-family:"Orbitron",Arial,sans-serif;font-weight:700;font-size:30px}
.footer-rule{position:absolute;left:160px;top:180px;width:880px;height:1px;background:#333}
.social{position:absolute;top:206px;width:68px;height:68px;border-radius:50%;border:2px solid #777;display:flex;align-items:center;justify-content:center;font-family:"Orbitron",Arial,sans-serif;font-size:12px;color:var(--white)}
.copyright{position:absolute;left:0;top:302px;width:1200px;text-align:center;font-size:11px;color:#cfcfcf}
</style>
</head>
<body>

<header class="block hero">
  <div class="hero-photo" role="img" aria-label="Portrait photo of the artist in warm low light"></div>
  <div class="topbar">
    <div class="brand"><span class="brand-dot"></span>DARVIN KOLTZ</div>
    <nav class="nav">
      <a class="active" style="left:577px">HOME</a>
      <a style="left:670px">MEDIA</a>
      <a style="left:762px">NEWS</a>
      <a style="left:858px">BIO</a>
      <a style="left:932px">JOIN</a>
      <a style="left:1012px">CONTACT</a>
    </nav>
  </div>
  <h1 class="hero-title">DARVIN KOLTZ</h1>
  <p class="hero-text">Sed ut perspiciatis unde omnis iste natus error sit voluptatem accusantium doloremque laudantium, totam rem aperiam, eaque ipsa quae ab illo inventore et quasi architecto beatae vitae dicta sunt explicabo.</p>
  <a class="btn-red" style="left:111px;top:497px;width:134px;height:48px">READ MORE</a>
</header>

<section aria-label="Media">
  <h2 class="section-title" style="top:718px">OUR MEDIA</h2>
  <div class="video-main" role="img" aria-label="Featured music video still, people seated around a table">
    <div class="play" style="left:331px;top:160px"><svg width="26" height="28" viewBox="0 0 26 28"><path d="M2 1 L25 14 L2 27 Z" fill="#fff"/></svg></div>
    <div class="video-bar"><i></i><b></b></div>
  </div>
  <div class="thumb" style="left:235px;width:230px;background:linear-gradient(135deg,#5a2a2a,#8e3a30,#2a1414)" role="img" aria-label="Video thumbnail, performers in a red lit room">
    <div class="play" style="left:95px;top:52px;width:40px;height:40px"><svg width="14" height="16" viewBox="0 0 26 28"><path d="M2 1 L25 14 L2 27 Z" fill="#fff"/></svg></div>
  </div>
  <div class="thumb" style="left:484px;width:235px;background:linear-gradient(135deg,#3a2418,#6a4a30,#1e140e)" role="img" aria-label="Video thumbnail, crowd outdoors">
    <div class="play" style="left:97px;top:52px;width:40px;height:40px"><svg width="14" height="16" viewBox="0 0 26 28"><path d="M2 1 L25 14 L2 27 Z" fill="#fff"/></svg></div>
  </div>
  <div class="thumb" style="left:736px;width:232px;background:linear-gradient(135deg,#5a2a14,#a0541e,#3a1a0e)" role="img" aria-label="Video thumbnail, single cover art in warm tones">
    <div class="play" style="left:96px;top:52px;width:40px;height:40px"><svg width="14" height="16" viewBox="0 0 26 28"><path d="M2 1 L25 14 L2 27 Z" fill="#fff"/></svg></div>
  </div>
</section>

<section class="block banner" style="top:1361px;height:640px;background:linear-gradient(180deg,#2c4a6e 0%,#3f6a92 45%,#1f3550 100%)" role="img" aria-label="Photo of the artist in sunglasses against a blue sky">
  <div class="banner-rule" style="top:306px"></div>
  <div class="banner-word" style="top:318px">NEWS</div>
  <div class="banner-rule" style="top:436px"></div>
</section>

<section class="block news" aria-label="News">
  <article class="card" style="left:111px">
    <div class="card-img" role="img" aria-label="News photo of the artist with a friend" style="background:linear-gradient(135deg,#6a5a3a,#c29a5a,#3a2a1a)"></div>
    <h3>SED UT PERSPICIATIS UNDE OMNIS ISTE</h3>
    <div class="date">Posted on 17 Jan 2016</div>
    <p>Nemo enim ipsam voluptatem quia voluptas sit aspernatur aut odit aut fugit, sed quia consequuntur magni dolores eos qui ratione voluptatem sequi nesciunt.</p>
    <a class="btn-line">READ MORE</a>
  </article>
  <article class="card" style="left:443px">
    <div class="card-img" role="img" aria-label="News photo collage from an event" style="background:linear-gradient(135deg,#4a5a3a,#b04a5a,#7a2a2a)"></div>
    <h3>SED UT PERSPICIATIS UNDE OMNIS ISTE</h3>
    <div class="date">Posted on 17 Jan 2016</div>
    <p>Nemo enim ipsam voluptatem quia voluptas sit aspernatur aut odit aut fugit, sed quia consequuntur magni dolores eos qui ratione voluptatem sequi nesciunt.</p>
    <a class="btn-line">READ MORE</a>
  </article>
  <article class="card" style="left:774px">
    <div class="card-img" role="img" aria-label="News photo from a recording session" style="background:linear-gradient(135deg,#5a5a5a,#8a7a6a,#2a2420)"></div>
    <h3>SED UT PERSPICIATIS UNDE OMNIS ISTE</h3>
    <div class="date">Posted on 17 Jan 2016</div>
    <p>Nemo enim ipsam voluptatem quia voluptas sit aspernatur aut odit aut fugit, sed quia consequuntur magni dolores eos qui ratione voluptatem sequi nesciunt.</p>
    <a class="btn-line">READ MORE</a>
  </article>
</section>

<section class="block banner" style="top:2555px;height:622px;background:linear-gradient(180deg,#1a2230 0%,#2e3a44 50%,#141a20 100%)" role="img" aria-label="Photo of the artist with a group of friends outdoors at dusk">
  <div class="banner-rule" style="top:300px"></div>
  <div class="banner-word" style="top:312px">BIO</div>
  <div class="banner-rule" style="top:430px"></div>
</section>

<section class="block bio" aria-label="Biography">
  <div class="portrait" role="img" aria-label="Round portrait photo of the artist"></div>
  <h2 class="bio-name">JHON SMITH</h2>
  <div class="bio-date">Posted on 17 Jan 2016</div>
  <p class="bio-text" style="top:170px">Sed ut perspiciatis unde omnis iste natus error sit voluptatem accusantium doloremque laudantium, totam rem aperiam, eaque ipsa quae ab illo inventore et quasi architecto beatae vitae dicta sunt explicabo. Nemo enim ipsam voluptatem quia voluptas sit aspernatur aut odit aut fugit, sed quia consequuntur magni dolores eos qui ratione voluptatem sequi nesciunt.</p>
  <p class="bio-text" style="top:304px">Neque porro quisquam est, qui dolorem ipsum quia dolor sit amet, consectetur, adipisci velit, sed quia non numquam eius modi tempora incidunt ut labore et dolore magnam aliquam quaerat voluptatem. Quis autem vel eum iure reprehenderit qui in ea voluptate.</p>
  <a class="btn-line" style="position:absolute;left:538px;top:402px;width:136px;height:50px">READ MORE</a>
</section>

<section class="block banner" style="top:3650px;height:586px;background:linear-gradient(180deg,#181410 0%,#3a2e22 45%,#0e0c0a 100%)" role="img" aria-label="Photo of people walking along a street at night">
  <div class="banner-rule" style="top:262px"></div>
  <div class="banner-word" style="top:274px">JOIN</div>
  <div class="banner-rule" style="top:392px"></div>
</section>

<section aria-label="Join the fan club">
  <p class="join-lead">Sed ut perspiciatis unde omnis iste natus erriv uptatem accusantium quasi architecto beatae vitae dicta sunt explicabo.</p>
  <div class="field" style="top:4376px">User Name</div>
  <div class="field" style="top:4432px">Email</div>
  <div class="field" style="top:4488px">Confirm Password</div>
  <div class="field" style="top:4544px">Message</div>
  <a class="btn-red" style="left:518px;top:4610px;width:166px;height:52px">JOIN NOW!</a>
</section>

<footer class="block footer">
  <div class="footer-brand"><span class="brand-dot"></span>DARVIN KOLTZ</div>
  <div class="footer-rule"></div>
  <a class="social" style="left:460px" aria-label="Facebook">FB</a>
  <a class="social" style="left:534px" aria-label="Twitter">TW</a>
  <a class="social" style="left:608px" aria-label="YouTube">YT</a>
  <a class="social" style="left:676px" aria-label="Instagram">IG</a>
  <div class="copyright">© Copyright 2016 · Darvin Koltz All Rights Reserved</div>
</footer>

</body>
</html>
```